依頼概要
■ 依頼の目的/概要

会社の名刺でデザイン製作をお願いします。

■ 名刺に記載する情報

表面:会社名/事業内容/役職/氏名/住所/電話/Fax/Mail

裏面:ショップロゴマーク(添付ファイル)/URL

■ 名刺デザインへの要望

ドレスやアクセサリー・服飾雑貨の輸入・製造・卸販売と実店舗・ネット通販をしている会社です。商材がドレスやアクセサリーなどですので、華やかでありつつもシンプルでスタイリッシュな仕事がデキル感じのするデザインをお願いします。
ほんの少しポップの要素がプラスされてもOKです。
※欲を言えば、(仕入れ・卸販売部門)と(実店舗・ネット通販販売部門)の色分け
やちょっとした雰囲気を変えて頂ければ最高です。
どうぞよろしくお願いします。

会社名 株式会社ラボミナセ

事業内容  ドレス・アクセサリー・服飾雑貨の輸入卸販売

■ 納品ファイルの希望

イラストレーター形式もしくはフォトショップ形式

■ 進め方

弊社の希望するイメージに近い提案を1つ(場合によって複数)選択させて頂きます。希望に近づけるために、修正要望を個別にさせて頂くこともあります。コンペ方式のため、修正後に当選されない場合も、どうかご了承ください。
よい提案があれば、早めに決定したいと思います。
不明な点がありましたら、お問い合わせください。

TULEのロゴマークに花のマークが付いているのですが、このお花のみのロゴは使用しないで下さい。どうぞよろしくお願い致します。
■ 選んだ理由

デザイン・文字がイメージ通りだったので決定させて頂きました。

■ 提案者全員のお礼・コメント

この度はご提案頂きまして誠に有難うございました。
最後まで決めるのを迷いました。素敵なご提案を多数頂きまして有難うございました

```html
<!DOCTYPE html>
<html lang="ja">
<head>
<meta charset="UTF-8">
<title>名刺 表面 — 株式会社ラボミナセ</title>
<link href="https://fonts.googleapis.com/css2?family=Arimo:wght@400&family=Noto+Sans+JP:wght@400;500;700&display=swap" rel="stylesheet">
<style>
  :root {
    --paper: #ffffff;
    --ink: #1a1a1a;
    --accent: #5cc6b6;
    --edge: #d6d6d6;
  }
  html, body {
    margin: 0;
    padding: 0;
    overflow: hidden;
    background: var(--paper);
  }
  .card {
    position: relative;
    width: 755px;
    height: 1200px;
    background: var(--paper);
    box-sizing: border-box;
    border: 2px solid var(--edge);
    overflow: hidden;
    color: var(--ink);
    font-family: "Noto Sans JP", sans-serif;
  }
  .card p { margin: 0; position: absolute; white-space: nowrap; line-height: 1; }
  .latin { font-family: "Arimo", "Noto Sans JP", sans-serif; }

  .name-ja {
    left: 236px; top: 252px;
    font-size: 44px; font-weight: 500;
    letter-spacing: 0.62em;
  }
  .name-en { left: 238px; top: 318px; font-size: 33px; letter-spacing: 0.02em; }

  .title-ja { left: 240px; top: 546px; font-size: 24px; }
  .title-en { left: 240px; top: 598px; font-size: 24px; }

  .company { left: 218px; top: 688px; font-size: 31px; font-weight: 500; }
  .address-ja { left: 218px; top: 740px; font-size: 25px; }
  .address-ja .postal { margin-right: 24px; }
  .company-en { left: 218px; top: 790px; font-size: 31px; }
  .address-en-1 { left: 300px; top: 842px; font-size: 25px; }
  .address-en-2 { left: 300px; top: 880px; font-size: 25px; }
  .email { left: 218px; top: 940px; font-size: 25px; }
  .phones { left: 218px; top: 990px; font-size: 25px; }
  .phones .fax { margin-left: 28px; }

  .business {
    left: 218px; top: 1090px;
    font-size: 25px; font-weight: 700;
    letter-spacing: 0.01em;
  }
  .accent-bar {
    position: absolute;
    left: 220px; top: 1126px;
    width: 540px; height: 12px;
    background: var(--accent);
  }
</style>
</head>
<body>
  <main class="card">
    <p class="name-ja">高瀬涼真</p>
    <p class="name-en latin">Ryoma Takase</p>

    <p class="title-ja">代表取締役</p>
    <p class="title-en latin">executive president</p>

    <p class="company">株式会社ラボミナセ</p>
    <p class="address-ja"><span class="postal latin">110-0011</span>東京都千代田区〇〇-〇〇</p>
    <p class="company-en latin">Labo Minase.INC</p>
    <p class="address-en-1 latin">〇〇-〇〇, Chiyoda-Ku</p>
    <p class="address-en-2 latin">Tokyo-To,110-0011,Japan</p>
    <p class="email latin">E-mail:takase@minase-labo.jp</p>
    <p class="phones latin"><span class="tel">TEL.03-000-0000</span><span class="fax">FAX.03-000-0001</span></p>

    <p class="business">ドレス・アクセサリー・服飾雑貨の輸入卸販売</p>
    <div class="accent-bar"></div>
  </main>
</body>
</html>
```